Landing Page

basically our company has as an strategy to sell our subscription product a set os pages normally in 4 steps
1 - We show that the "customer" will win a prizze
2 - We show some advantages that we have as a company
3 - We show another prizze
4 - We explain that to gain all itens they should make a subscription with a HUGE discount
What do we need?
1 - a new proposal for our set of landing pages
2 - responsive layout for all pages
3 - ideas that can increase our conversion rates
Examples:
http://www.descubravantagens.com/
http://www.descubravantagens.com/vistacam/index.php
http://www.descubravantagens.com/brightdeals/index.php
http://www.descubravantagens.com/v2/index.php
http://atendimentogeral.avaliamos.org.br/index.aspx?prm_id_c=KXR27004
http://www.premiavela.com.br/br_tmk_pro_vsi_int_1.asp?mktcode=TMQW72
https://www.bridgeloop480.info/seq2012/twosteps/pt_br/b2013/index.html?lang=brpt_br&project=TwoSteps&codeprom=FJUB4702&tmpl=b2013&cn=AB11CD22-33EF-4A5B-8C6D-7E8F9A0B1C2D#1
https://atendimentogeral.avaliamos.org.br/step_03.aspx
It Company

```html
<!DOCTYPE html>
<html lang="en">
<head>
<meta charset="utf-8">
<title>Avaliamos – Landing</title>
<link href="https://fonts.googleapis.com/css2?family=Open+Sans:wght@400;600;700&display=swap" rel="stylesheet">
<style>
:root{
  --green:#92c300;
  --green-dark:#7aae00;
  --green-text:#7cb500;
  --ink:#333;
  --muted:#6b6b6b;
  --light:#f4f4f4;
  --white:#fff;
  --sky-top:#a9d3f2;
  --sky-low:#dcedf8;
  --grass:#8cbf3a;
}
*{box-sizing:border-box;margin:0;padding:0}
html,body{width:1011px;height:1200px;overflow:hidden}
body{font-family:"Open Sans",Arial,sans-serif;color:var(--ink);position:relative;background:var(--white)}
.hero{position:absolute;left:0;top:0;width:1011px;height:522px;
  background:linear-gradient(180deg,var(--sky-top) 0%,var(--sky-low) 70%,#c8dfb0 82%,var(--grass) 90%,#6ea52a 100%)}
.topbar{position:absolute;top:14px;left:112px;font-size:8.5px;color:#555}
.topbar a{color:#555;text-decoration:none}
.topbar span{margin:0 5px}
.search{position:absolute;left:642px;top:10px;width:174px;height:19px;background:var(--white);border:1px solid #ddd;font-size:8px;color:#bbb;padding:3px 4px}
.search svg{position:absolute;right:4px;top:3px}
.register{position:absolute;left:822px;top:8px;width:76px;height:23px;background:var(--green);border-radius:2px;color:var(--white);font-size:10px;font-weight:700;text-align:center;line-height:23px;border:1px solid var(--green-dark)}
.header{position:absolute;left:110px;top:38px;width:789px;height:73px;background:linear-gradient(#fff,#f1f1f1);border-bottom:2px solid #cfd6db;border-radius:2px}
.brand{position:absolute;left:18px;top:22px;font-size:23px;font-weight:700;color:#2e7d10;letter-spacing:-.5px;display:flex;align-items:center;gap:6px}
.brand i{display:block;width:10px;height:10px;border-radius:50%;background:var(--green)}
.nav{position:absolute;right:10px;top:29px;display:flex;gap:18px;font-size:11.5px;font-weight:700;color:#333}
.nav .active{color:var(--green)}
.signup{position:absolute;left:644px;top:154px;width:256px;height:267px;background:rgba(255,255,255,.92);border-radius:3px;padding:18px 20px}
.signup h3{font-size:12.5px;color:var(--green-text);font-weight:700}
.gender{display:flex;gap:50px;margin-top:10px;font-size:9px;color:#555}
.gender label{display:flex;align-items:center;gap:8px}
.box{width:10px;height:10px;border:1px solid #999;background:#fff;position:relative}
.field{margin-top:14px;height:35px;border:1px solid #ddd;background:#fff;font-size:8.5px;color:#888;padding:11px 8px}
.field+.field{margin-top:9px}
.btn{display:block;margin:18px auto 0;width:91px;height:28px;background:var(--green);border:1px solid var(--green-dark);color:#fff;font-size:10px;text-align:center;line-height:27px;border-radius:2px}
.terms{margin-top:15px;font-size:8px;line-height:17px;color:#555;text-align:justify}
.dots{position:absolute;top:484px;left:467px;display:flex;gap:7px}
.dots b{width:13px;height:13px;border-radius:50%;background:#222}
.dots b:first-child{background:#556b1a}
.steps{position:absolute;left:0;top:522px;width:1011px;height:200px;background:var(--green);color:#fff}
.steps svg{position:absolute;left:0;top:0;overflow:visible}
.step{position:absolute;top:95px;width:190px}
.step h4{font-size:12px;font-weight:700}
.step p{margin-top:14px;font-size:10.5px;line-height:20px}
.perks{position:absolute;left:0;top:722px;width:1011px;height:148px;background:var(--light);border-bottom:1px solid #e6e6e6}
.perk{position:absolute;top:36px;width:254px}
.perk h3,.col h3{font-size:12.5px;color:var(--green-text);font-weight:700}
.perk .art{position:absolute;top:28px;left:0;width:60px;height:50px;border-radius:4px}
.perk p{margin:22px 0 0 70px;font-size:8.3px;line-height:15.2px;color:#666;text-align:justify}
.col{position:absolute;top:896px}
.news p{font-size:8.3px;line-height:18px;color:#222}
.news p.sub{color:#666}
.news .item{margin-top:14px}
.news .item+.item{margin-top:16px}
.quote{font-size:8.3px;line-height:16.6px;color:#666;text-align:justify}
.quote b{display:block;color:var(--green-text);font-weight:600;margin-top:14px}
.quote b+span{display:block;margin-top:1px}
.features{list-style:none;margin-top:20px}
.features li{display:flex;align-items:center;height:24.8px;font-size:10px;color:#333}
.features svg{margin-right:27px}
.footer{position:absolute;left:0;top:1126px;width:1011px;height:74px;background:var(--green);color:#fff}
.footer .info{position:absolute;left:112px;top:10px;font-size:10px;line-height:20px}
.footer .info strong{font-weight:700}
.footer .links{position:absolute;left:627px;top:35px;font-size:10.5px;font-weight:700}
.footer .links span{margin:0 9px}
</style>
</head>
<body>
<div class="hero" role="img" aria-label="Photo of a woman sitting on a grassy field working on a laptop under a clear blue sky"></div>

<nav class="topbar"><a>About Us</a><span>|</span><a>What We Offer</a><span>|</span><a>Join</a><span>|</span><a>Contact</a><span>|</span><a>Press</a></nav>
<div class="search">Search
  <svg width="12" height="12" viewBox="0 0 12 12"><circle cx="4.5" cy="4.5" r="3.3" fill="none" stroke="#444" stroke-width="1.4"/><line x1="7" y1="7" x2="11" y2="11" stroke="#444" stroke-width="2"/></svg>
</div>
<div class="register">REGISTER</div>

<header class="header">
  <div class="brand"><i></i>AVALIAMOS</div>
  <nav class="nav"><span class="active">HOME</span><span>FEED</span><span>CARS</span><span>MONEY</span><span>APPLIANCES</span><span>FAMILY</span><span>HEALTH</span><span>TECHNOLOGY</span></nav>
</header>

<form class="signup">
  <h3>SIGN UP HERE</h3>
  <div class="gender">
    <label><span class="box"></span>Male</label>
    <label><span class="box"><svg width="10" height="10" viewBox="0 0 10 10" style="position:absolute;left:0;top:-1px"><path d="M2 5l2 3 5-7" fill="none" stroke="#2c5aa0" stroke-width="1.6"/></svg></span>Fe-Male</label>
  </div>
  <div class="field">Name</div>
  <div class="field">E-Mail</div>
  <div class="btn">SIGN UP</div>
  <p class="terms">I understand that by signing up, I shall receive product offerings and AVALIAMOS and its partners.</p>
</form>

<div class="dots"><b></b><b></b><b></b><b></b></div>

<section class="steps">
  <svg width="1011" height="100" viewBox="0 0 1011 100">
    <line x1="133" y1="63" x2="902" y2="63" stroke="#fff" stroke-width="6" stroke-linecap="round"/>
    <g fill="var(--green)" stroke="#fff" stroke-width="5">
      <circle cx="133" cy="62" r="21"/><circle cx="337" cy="63" r="21"/><circle cx="540" cy="63" r="21"/><circle cx="742" cy="64" r="21"/>
    </g>
    <g fill="#fff" font-family="Open Sans, sans-serif" font-size="22" font-weight="600" text-anchor="middle">
      <text x="133" y="70">1</text><text x="337" y="71">2</text><text x="540" y="71">3</text><text x="742" y="72">4</text>
    </g>
  </svg>
  <div class="step" style="left:110px"><h4 style="margin-left:5px">STEP 1</h4><p>We show that the <b>"CUSTOMER"</b> will win a prize</p></div>
  <div class="step" style="left:311px"><h4 style="margin-left:3px">STEP 2</h4><p>We show some advantages that we have as a <b>COMPANY</b></p></div>
  <div class="step" style="left:512px"><h4 style="margin-left:9px">STEP 3</h4><p>We show another <b>PRIZE</b></p></div>
  <div class="step" style="left:717px"><h4 style="margin-left:6px">STEP 4</h4><p>We explain that to gain all items they should make a subscription with a <b>HUGE</b> discount</p></div>
</section>

<section class="perks">
  <div class="perk" style="left:109px"><h3>GRANTA THEIR RIGHTS</h3>
    <div class="art" role="img" aria-label="Illustration of a wooden judge's gavel" style="background:#8a4a2a"></div>
    <p>By joining AVALIAMOS you will have access to various information that will help you make your claims and defend their rights as a consumer.</p></div>
  <div class="perk" style="left:379px"><h3>RECEIVE THE PUBLICATIONS</h3>
    <div class="art" role="img" aria-label="Illustration of a consumer magazine cover" style="background:#b8463c"></div>
    <p>By joining AVALIAMOS you will have access to various information that will help you make your claims and defend their rights as a consumer.</p></div>
  <div class="perk" style="left:649px"><h3>WIN A SURPRISE</h3>
    <div class="art" role="img" aria-label="Illustration of an open gift box with a teal ribbon" style="background:#7fd0d8"></div>
    <p>By joining AVALIAMOS you will have access to various information that will help you make your claims and defend their rights as a consumer.</p></div>
</section>

<section class="col news" style="left:108px;width:245px">
  <h3>LATEST &nbsp;NEWS</h3>
  <div class="item"><p>Lorem Ipsum is simply dummy text of the printing and typesetting industry.</p><p class="sub">Lorem Ipsum has been the industry's standard dummy text ever since the 1500s, when an unknown printer took</p></div>
  <div class="item"><p>Lorem Ipsum is simply dummy text of the printing and typesetting industry.</p><p class="sub">Lorem Ipsum has been the industry's standard dummy text ever since the 1500s, when an unknown printer took</p></div>
</section>

<section class="col" style="left:379px;width:220px">
  <h3>QUAM APROVOU A AVALIAMOS</h3>
  <div class="quote">
    <b>Marina Quintela</b><span>Always had many questions about my rights as a consumer. With AVALIAMOS, I had access to lots of content and I feel more prepared today to claim when I am injured.</span>
    <b>Davi Monteiro</b><span>'ve been through many situations where I thought that my rights were not respected and not sure how to proceed. The advice of AVALIAMOS makes all the difference!</span>
  </div>
</section>

<section class="col" style="left:648px;width:260px">
  <h3>FEATURED PRODUCT</h3>
  <ul class="features">
    <li><svg width="21" height="20" viewBox="0 0 21 20"><path d="M2 11l5 6L19 2" fill="none" stroke="var(--green)" stroke-width="3.2" stroke-linecap="round" stroke-linejoin="round"/></svg>2.0M CMOS Sensor</li>
    <li><svg width="21" height="20" viewBox="0 0 21 20"><path d="M2 11l5 6L19 2" fill="none" stroke="var(--green)" stroke-width="3.2" stroke-linecap="round" stroke-linejoin="round"/></svg>Screen 1.8-inch TFT LCD</li>
    <li><svg width="21" height="20" viewBox="0 0 21 20"><path d="M2 11l5 6L19 2" fill="none" stroke="var(--green)" stroke-width="3.2" stroke-linecap="round" stroke-linejoin="round"/></svg>4x Digital Zoom</li>
    <li><svg width="21" height="20" viewBox="0 0 21 20"><path d="M2 11l5 6L19 2" fill="none" stroke="var(--green)" stroke-width="3.2" stroke-linecap="round" stroke-linejoin="round"/></svg>3 MP resolution photo (JPG)</li>
    <li><svg width="21" height="20" viewBox="0 0 21 20"><path d="M2 11l5 6L19 2" fill="none" stroke="var(--green)" stroke-width="3.2" stroke-linecap="round" stroke-linejoin="round"/></svg>Accompanying USB cable</li>
    <li><svg width="21" height="20" viewBox="0 0 21 20"><path d="M2 11l5 6L19 2" fill="none" stroke="var(--green)" stroke-width="3.2" stroke-linecap="round" stroke-linejoin="round"/></svg>Works with SD card (not included)</li>
  </ul>
</section>

<footer class="footer">
  <div class="info"><strong>2013 AVALIAMOS</strong><br>Independência, Proximidade e Excelência<br>Rua das Palmeiras, 1.280 - Jardim Aurora - Rio de Janeiro</div>
  <div class="links">PRIVACIDADE<span>|</span>TERMOS E CONDIÇÕES<span>|</span>CONTATO</div>
</footer>
</body>
</html>
```